Brisk Lumo Entertainment

I need a web design for my Business for better online promotions and services.. The name of my company is Brisk Lumo its a entertainment company music, events, networking and so on.. What I do is help artist create and finish projects such as mix tapes, music videos, and book performances in order to create a platform and i also offer representation to help grow there brands or business... I also work with and help develop independent artists!!!

Target Market(s)

Hip hop and R&B industry

Industry/Entity Type

Entertainment Industry

Number of Pages Required

1 page

Requirements
Must have
• Must display My previous and upcoming work i want people to see the quality I provide in my service.. I have more videos that I want to upload on there to show more work.... I would like to bring all the separate promotions and campaigns that I previously had and currently have all one platform for everybody to see and to find more easily instead having everything so spread out..
Nice to have
• Creativity thats going to compliment my work and quality..

```html
<!DOCTYPE html>
<html lang="en">
<head>
<meta charset="utf-8">
<title>Brisk Lumo Entertainment</title>
<link href="https://fonts.googleapis.com/css2?family=Jost:wght@400;500&family=Open+Sans:wght@400;600&display=swap" rel="stylesheet">
<style>
:root{
  --red:#d4232c;
  --red-dark:#8a1017;
  --ink:#2a2a2a;
  --muted:#777;
  --line:#e2e2e2;
  --night:#1c1c1f;
  --night-2:#141416;
  --white:#fff;
}
*{box-sizing:border-box;margin:0;padding:0}
html,body{width:1200px;height:3248px;overflow:hidden}
body{font-family:"Open Sans",sans-serif;color:var(--ink);background:var(--white);position:relative}
.heading{font-family:"Jost",sans-serif;font-weight:400}

/* Hero */
.hero{position:absolute;left:0;top:0;width:1200px;height:772px;
  background:radial-gradient(ellipse at 50% 30%,#6a1a22 0%,#3a0f14 45%,#140708 100%)}
.hero-photo{position:absolute;inset:0;background:linear-gradient(180deg,rgba(0,0,0,.15),rgba(0,0,0,.45))}
.brand{position:absolute;left:0;width:1200px;top:190px;text-align:center;font-family:"Jost",sans-serif;font-size:52px;font-weight:500;color:var(--red);letter-spacing:2px}
.brand .mark{display:inline-block;width:18px;height:18px;background:var(--red);margin-right:14px;vertical-align:middle}
.nav{position:absolute;top:306px;left:0;width:1200px;display:flex;justify-content:center;gap:58px;font-size:18px;color:var(--white)}
.tagline{position:absolute;top:428px;width:1200px;text-align:center;color:var(--white);font-size:40px}
.btn-red{position:absolute;left:484px;top:520px;width:236px;height:58px;background:var(--red);color:var(--white);font-size:19px;font-weight:600;display:flex;align-items:center;justify-content:center;gap:12px;border-radius:3px}
.btn-red .dot{width:22px;height:22px;border-radius:50%;background:var(--white);display:inline-flex;align-items:center;justify-content:center}
.slider-dots{position:absolute;right:40px;top:352px;display:flex;flex-direction:column;gap:10px}
.slider-dots span{width:12px;height:12px;border-radius:50%;border:2px solid var(--white)}
.slider-dots span.on{background:var(--red);border-color:var(--red)}

/* Welcome */
.welcome-title{position:absolute;left:120px;top:800px;font-size:42px;color:var(--red)}
.welcome-sub{position:absolute;left:120px;top:854px;font-size:17px;font-weight:600}
.welcome-text{position:absolute;left:120px;top:906px;width:540px;font-size:13.5px;line-height:24px;color:var(--muted)}
.btn-outline{position:absolute;left:120px;top:1068px;width:176px;height:52px;border:2px solid var(--red);color:var(--ink);font-size:16px;font-weight:600;display:flex;align-items:center;justify-content:center;gap:10px;border-radius:4px}
.btn-outline .dot{width:20px;height:20px;border-radius:50%;background:var(--red)}
.cover{position:absolute;left:716px;top:748px;width:368px;height:412px;background:linear-gradient(160deg,#2e4a1a,#0f1a0a 60%,#1e0c0c);box-shadow:0 6px 18px rgba(0,0,0,.3)}

/* Section titles */
.section-title{position:absolute;left:0;width:1200px;text-align:center;font-size:42px;color:var(--red)}

/* Videos */
.video{position:absolute;width:468px;height:328px;border-radius:8px;overflow:hidden}
.video .play{position:absolute;left:50%;top:50%;width:52px;height:52px;margin:-26px 0 0 -26px;border-radius:50%;background:var(--red);display:flex;align-items:center;justify-content:center}
.v1{left:124px;top:1360px;background:linear-gradient(160deg,#4a3a2e,#1a140f)}
.v2{left:656px;top:1360px;background:linear-gradient(160deg,#3a4a6a,#12151f)}
.v3{left:124px;top:1728px;background:linear-gradient(160deg,#3e3a36,#141210)}
.v4{left:656px;top:1728px;background:linear-gradient(160deg,#234a1c,#0b1308)}

/* Music */
.tabs{position:absolute;top:2252px;left:0;width:1200px;display:flex;justify-content:center;gap:44px;font-size:19px}
.tabs .active{color:var(--red)}
.playlist-line{position:absolute;left:158px;top:2350px;width:2px;height:290px;background:var(--line)}
.avatar{position:absolute;left:154px;width:86px;height:86px;border-radius:50%;background:linear-gradient(135deg,#c98a5a,#3a2416);border:3px solid var(--white);box-shadow:0 0 0 2px var(--line)}
.pin{position:absolute;left:153px;width:12px;height:12px;border-radius:50%;background:var(--red)}
.player{position:absolute;left:356px;top:2340px;width:448px;height:190px}
.player .artist{font-size:15px;font-weight:600;color:var(--ink)}
.player .label{position:absolute;left:230px;top:0;font-size:15px;color:var(--ink)}
.player .track{font-size:15px;color:var(--ink);margin-top:6px}
.player svg{position:absolute;left:0;top:78px}
.player-meta{position:absolute;left:356px;top:2544px;display:flex;gap:26px;font-size:12px;color:var(--muted)}
.album{position:absolute;left:832px;top:2312px;width:288px;height:288px;background:linear-gradient(160deg,#f2e6b8,#d8b24a 60%,#6a2a1a);box-shadow:0 4px 14px rgba(0,0,0,.2)}

/* Footer */
.footer{position:absolute;left:0;top:2720px;width:1200px;height:528px;background:var(--night);color:var(--white)}
.footer-title{position:absolute;top:94px;width:1200px;text-align:center;font-size:34px}
.contact{position:absolute;left:256px;top:186px;display:flex;flex-direction:column;gap:32px;font-size:16px}
.contact li{list-style:none;display:flex;align-items:center;gap:26px}
.form{position:absolute;left:720px;top:186px;width:228px;font-size:14px}
.form .field{border-bottom:1px solid #555;height:56px;padding-top:4px}
.form .field.tall{height:64px}
.send{position:absolute;left:844px;top:372px;width:96px;height:32px;background:var(--red);display:flex;align-items:center;justify-content:center;font-size:15px}
.footer-brand{position:absolute;left:236px;top:346px;font-family:"Jost",sans-serif;font-size:46px;font-weight:500;color:var(--red);letter-spacing:2px}
.copyright{position:absolute;left:0;top:476px;width:1200px;height:52px;background:var(--night-2);text-align:center;line-height:52px;font-size:11px;color:#999}
</style>
</head>
<body>

<header class="hero">
  <div class="hero-photo" role="img" aria-label="DJ performing at turntables under red stage lights"></div>
  <div class="brand"><span class="mark"></span>Brisk Lumo</div>
  <nav class="nav"><span>Home</span><span>About Us</span><span>Team</span><span>Music</span><span>Contact Us</span></nav>
  <h1 class="tagline heading">Lets Enjoy Your Day With Us</h1>
  <div class="btn-red">Download Now <span class="dot"><svg width="10" height="10" viewBox="0 0 10 10"><path d="M3 1l4 4-4 4" stroke="#d4232c" stroke-width="2" fill="none"/></svg></span></div>
  <div class="slider-dots"><span class="on"></span><span></span><span></span></div>
</header>

<section class="welcome">
  <h2 class="welcome-title heading">Welcome To Brisk Lumo</h2>
  <p class="welcome-sub">Make Our Appointment</p>
  <p class="welcome-text">We help independent artists shape raw ideas into finished mixtapes, music videos and live shows. From the first session in the studio to the last note on stage, our team handles recording, booking and brand growth so every release lands with quality. Book a meeting and let us plan your next project together with care and focus.</p>
  <div class="btn-outline">Show Details <span class="dot"></span></div>
  <div class="cover" role="img" aria-label="Mixtape cover artwork with artist under green light"></div>
</section>

<section class="videos">
  <h2 class="section-title heading" style="top:1264px">Check Out Our Videos</h2>
  <div class="video v1" role="img" aria-label="Music video still of artist"><span class="play"><svg width="18" height="18" viewBox="0 0 18 18"><path d="M5 3l10 6-10 6z" fill="#fff"/></svg></span></div>
  <div class="video v2" role="img" aria-label="Music video still of two artists"><span class="play"><svg width="18" height="18" viewBox="0 0 18 18"><path d="M5 3l10 6-10 6z" fill="#fff"/></svg></span></div>
  <div class="video v3" role="img" aria-label="Music video still of group of artists"><span class="play"><svg width="18" height="18" viewBox="0 0 18 18"><path d="M5 3l10 6-10 6z" fill="#fff"/></svg></span></div>
  <div class="video v4" role="img" aria-label="Music video thumbnail for mixtape release"><span class="play"><svg width="18" height="18" viewBox="0 0 18 18"><path d="M5 3l10 6-10 6z" fill="#fff"/></svg></span></div>
</section>

<section class="music">
  <h2 class="section-title heading" style="top:2172px">Listen To Our Music</h2>
  <div class="tabs"><span class="active">All</span><span>Tracks</span><span>Albums</span></div>
  <div class="playlist-line"></div>
  <div class="avatar" style="top:2318px" role="img" aria-label="Artist avatar"></div>
  <div class="pin" style="top:2354px;left:236px"></div>
  <div class="avatar" style="top:2446px" role="img" aria-label="Artist avatar"></div>
  <div class="avatar" style="top:2566px" role="img" aria-label="Artist avatar"></div>
  <div class="player">
    <div class="artist">Velvet Ray</div>
    <div class="label">Brisk Lumo Music Ent</div>
    <div class="track">Late Night Drive (Prod. By Kay Roe)</div>
    <svg width="448" height="100" viewBox="0 0 448 100">
      <g fill="#bbb">
        <rect x="0" y="40" width="4" height="40"/><rect x="8" y="30" width="4" height="50"/><rect x="16" y="44" width="4" height="36"/><rect x="24" y="26" width="4" height="54"/><rect x="32" y="36" width="4" height="44"/><rect x="40" y="20" width="4" height="60"/><rect x="48" y="34" width="4" height="46"/><rect x="56" y="24" width="4" height="56"/><rect x="64" y="40" width="4" height="40"/><rect x="72" y="28" width="4" height="52"/><rect x="80" y="18" width="4" height="62"/><rect x="88" y="32" width="4" height="48"/><rect x="96" y="22" width="4" height="58"/><rect x="104" y="38" width="4" height="42"/><rect x="112" y="26" width="4" height="54"/><rect x="120" y="34" width="4" height="46"/><rect x="128" y="20" width="4" height="60"/><rect x="136" y="42" width="4" height="38"/><rect x="144" y="30" width="4" height="50"/><rect x="152" y="24" width="4" height="56"/><rect x="160" y="36" width="4" height="44"/><rect x="168" y="28" width="4" height="52"/><rect x="176" y="40" width="4" height="40"/><rect x="184" y="22" width="4" height="58"/><rect x="256" y="32" width="4" height="48"/><rect x="264" y="20" width="4" height="60"/><rect x="272" y="38" width="4" height="42"/><rect x="280" y="26" width="4" height="54"/><rect x="288" y="34" width="4" height="46"/><rect x="296" y="18" width="4" height="62"/><rect x="304" y="40" width="4" height="40"/><rect x="312" y="28" width="4" height="52"/><rect x="320" y="36" width="4" height="44"/><rect x="328" y="24" width="4" height="56"/><rect x="336" y="42" width="4" height="38"/><rect x="344" y="30" width="4" height="50"/><rect x="352" y="22" width="4" height="58"/><rect x="360" y="38" width="4" height="42"/><rect x="368" y="28" width="4" height="52"/><rect x="376" y="44" width="4" height="36"/><rect x="384" y="34" width="4" height="46"/><rect x="392" y="40" width="4" height="40"/><rect x="400" y="48" width="4" height="32"/><rect x="408" y="52" width="4" height="28"/>
      </g>
      <rect x="0" y="80" width="420" height="3" fill="#ddd"/>
      <circle cx="220" cy="46" r="26" fill="#d4232c"/>
      <path d="M213 34l18 12-18 12z" fill="#fff"/>
      <rect x="420" y="64" width="28" height="16" fill="#333"/>
    </svg>
  </div>
  <div class="player-meta"><span>♥ 129</span><span>⟳ 12</span><span>Share</span><span>More</span></div>
  <div class="album" role="img" aria-label="Album cover artwork with champagne bottle"></div>
</section>

<footer class="footer">
  <h2 class="footer-title heading">Get In Touch</h2>
  <ul class="contact">
    <li><svg width="16" height="16" viewBox="0 0 16 16"><path d="M2 8l6-6 6 6v6H2z" fill="#fff"/></svg>Brisk Lumo, Australia</li>
    <li><svg width="16" height="16" viewBox="0 0 16 16"><path d="M4 1h8v14H4z" fill="none" stroke="#fff" stroke-width="2"/></svg>0400 123 456</li>
    <li><svg width="16" height="16" viewBox="0 0 16 16"><rect x="1" y="3" width="14" height="10" fill="#fff"/><path d="M1 3l7 6 7-6" stroke="#1c1c1f" fill="none"/></svg>hello@brisklumo.example</li>
  </ul>
  <div class="form">
    <div class="field">Name</div>
    <div class="field">Email</div>
    <div class="field tall">Message</div>
  </div>
  <div class="send">Send</div>
  <div class="footer-brand">Brisk Lumo</div>
  <div class="copyright">© 2017 Brisk Lumo All rights reserved. Terms of Use</div>
</footer>

</body>
</html>
```